Capability statement graphic design documement

We have written a capability statement for our training business, we would like someone to really make it professional and stand out.

Target Market(s)

Engineering, ports and mining companies

Industry/Entity Type

Coal Mining

Font styles to use
Sans Serif

Colors
9bcb3c

Requirements
Must have
• Very good visual designs.
I have included a couple of example such as the TR Harbour capability statement which has good designs.
Our colours are green, black, white, grey. Our logos are uploaded.

```html
<!DOCTYPE html>
<html lang="en">
<head>
<meta charset="utf-8">
<title>Vantage Skills – Capability Statement</title>
<link href="https://fonts.googleapis.com/css2?family=Montserrat:wght@400;600;700;800&family=Open+Sans:wght@400;600;700&display=swap" rel="stylesheet">
<style>
:root{
  --green:#9bcb3c;
  --green-dark:#5f8f1c;
  --black:#1b1b1b;
  --grey:#6d6d6d;
  --grey-light:#e6e6e6;
  --paper:#ffffff;
  --canvas:#f1f1f1;
}
*{box-sizing:border-box;margin:0;padding:0}
html,body{width:1200px;height:2632px;overflow:hidden;background:var(--canvas);font-family:"Open Sans",Arial,sans-serif;color:var(--black)}
.canvas{position:relative;width:1200px;height:2632px}
.page{position:absolute;width:496px;height:720px;background:var(--paper);box-shadow:0 4px 14px rgba(0,0,0,.18);overflow:hidden}
.page--cover{left:84px;top:80px}
.page--details{left:632px;top:80px}
.page--about{left:84px;top:1060px}
.page--people{left:632px;top:1060px}
.page--back{left:352px;top:1900px}

.brand{position:absolute;display:flex;align-items:center;gap:7px;font-family:"Montserrat",Arial,sans-serif;font-weight:800;font-size:13px;color:var(--green-dark);letter-spacing:.5px}
.brand__dot{width:20px;height:20px;border-radius:50%;background:var(--green)}
.photo{position:absolute}

.footer{position:absolute;left:0;bottom:0;width:100%;height:24px;background:var(--green);display:flex;justify-content:space-between;align-items:center;padding:0 26px;font-size:6px;color:#fff}
.footer::before{content:"";position:absolute;left:0;top:-4px;width:100%;height:4px;background:var(--black)}

.cover__title{position:absolute;left:34px;top:520px;font-family:"Montserrat",Arial,sans-serif;line-height:1}
.cover__title .l1{display:block;font-size:40px;font-weight:600;color:var(--grey);letter-spacing:1px}
.cover__title .l2{display:block;font-size:40px;font-weight:800;color:var(--green);letter-spacing:1px;margin-top:2px}
.cover__rule{position:absolute;left:34px;top:618px;width:430px;height:1px;background:var(--grey-light)}
.cover__web{position:absolute;left:34px;top:626px;font-size:7px;color:var(--grey)}

.section-title{position:absolute;left:34px;top:36px;font-family:"Montserrat",Arial,sans-serif;font-weight:800;font-size:17px;color:var(--green-dark)}
.section-sub{position:absolute;left:34px;top:60px;font-family:"Montserrat",Arial,sans-serif;font-weight:700;font-size:9px;color:var(--black)}
.section-rule{position:absolute;left:34px;top:58px;width:430px;height:2px;background:var(--green)}

.details-table{position:absolute;left:34px;top:82px;width:430px;border-collapse:collapse;font-size:6.5px}
.details-table td{padding:5px 8px;border-bottom:1px solid var(--grey-light)}
.details-table td:first-child{width:120px;font-weight:700;background:#f6f6f6}

.col{position:absolute;font-size:6.5px;line-height:1.6;color:#333}
.col p{margin-bottom:7px}
.ticks{list-style:none;margin-bottom:8px}
.ticks li{position:relative;padding-left:12px;margin-bottom:3px}
.ticks li::before{content:"";position:absolute;left:0;top:2px;width:6px;height:6px;background:var(--green);border-radius:1px}

.person__name{position:absolute;left:34px;top:82px;font-family:"Montserrat",Arial,sans-serif;font-size:9px;font-weight:700;color:var(--green-dark)}
.person__name span{color:var(--grey);font-weight:600}
.person__label{font-family:"Montserrat",Arial,sans-serif;font-weight:700;font-size:7px;color:var(--black);margin-bottom:3px}

.back__contact{position:absolute;left:70px;top:628px;width:360px;display:grid;grid-template-columns:1fr 1fr;gap:10px 20px;font-size:7px;color:var(--grey)}
.back__contact div{display:flex;align-items:center;gap:6px}
.back__contact svg{flex:none}
</style>
</head>
<body>
<div class="canvas">

  <!-- Cover -->
  <section class="page page--cover">
    <div class="brand" style="left:34px;top:26px"><span class="brand__dot"></span>VANTAGE SKILLS</div>
    <div class="photo" role="img" aria-label="Silhouettes of two workers on scaffolding against a golden sky" style="left:0;top:70px;width:496px;height:340px;background:linear-gradient(160deg,#e0c57a 0%,#a48744 45%,#3a3226 100%)"></div>
    <svg class="photo" style="left:0;top:70px" width="496" height="340" viewBox="0 0 496 340">
      <polygon points="0,0 60,0 0,90" fill="#9bcb3c"/>
      <polygon points="0,110 40,0 52,0 0,140" fill="#5f8f1c"/>
      <polygon points="496,300 496,340 380,340" fill="#9bcb3c"/>
    </svg>
    <h1 class="cover__title"><span class="l1">CAPABILITY</span><span class="l2">STATEMENT</span></h1>
    <div class="cover__rule"></div>
    <div class="cover__web">www.vantageskills.com.au</div>
    <div class="footer"><span></span><span></span></div>
  </section>

  <!-- Company details -->
  <section class="page page--details">
    <h2 class="section-title">1. COMPANY DETAILS</h2>
    <div class="section-rule"></div>
    <h3 class="section-sub" style="top:66px">CONTACT DETAILS</h3>
    <table class="details-table" style="top:84px">
      <tr><td>Company Name</td><td>Vantage Skills Training Pty Ltd</td></tr>
      <tr><td>ABN</td><td>42 118 506 734</td></tr>
      <tr><td>RTO</td><td>Registered Training Organisation 31842</td></tr>
      <tr><td>Telephone</td><td>(07) 4950 2218</td></tr>
      <tr><td>Email</td><td>admin@vantageskills.com.au</td></tr>
      <tr><td>Website</td><td>www.vantageskills.com.au</td></tr>
      <tr><td>Office Address</td><td>12 Harbour Road, Mackay QLD 4740</td></tr>
      <tr><td>Contact</td><td>Dana Whitlock, General Manager</td></tr>
    </table>
    <div class="photo" role="img" aria-label="Trainees working at height on a red elevated work platform beside green scaffolding" style="left:34px;top:330px;width:430px;height:330px;background:linear-gradient(180deg,#8fb3c9 0%,#6e8f4a 55%,#4d6b2e 100%)"></div>
    <div class="footer"><span>www.vantageskills.com.au</span><span>Page 02</span></div>
  </section>

  <!-- About us -->
  <section class="page page--about">
    <h2 class="section-title">2. ABOUT US</h2>
    <div class="section-rule"></div>
    <div class="col" style="left:34px;top:72px;width:205px">
      <p>Vantage Skills is a registered training provider delivering practical, high-risk and safety training to engineering, port and mining operators across regional Queensland.</p>
      <p><b>Our trainers bring decades of field experience to every course, on our site or yours.</b></p>
      <ul class="ticks">
        <li>Cranes</li><li>Elevated work platforms</li><li>Forklifts</li><li>Work at height</li><li>Confined space entry</li><li>Gas test atmospheres</li><li>Rigging and dogging</li>
      </ul>
      <p>We tailor each program to client procedures and site conditions.</p>
      <ul class="ticks">
        <li>Licence assessments</li><li>Verification of competency</li><li>Refresher training</li><li>Induction programs</li><li>Skills gap audits</li><li>Onsite delivery</li>
      </ul>
    </div>
    <div class="col" style="left:259px;top:72px;width:205px">
      <p>Our team works closely with site supervisors to plan training around production needs and shift rosters, keeping downtime low.</p>
      <ul class="ticks">
        <li>Nationally recognised units delivered to the current training package standards.</li>
        <li>Modern equipment and a purpose-built yard for safe practical assessment.</li>
        <li>Clear records and reporting for every learner and every client.</li>
      </ul>
      <p>Our trainers hold current industry tickets and maintain their own skills through regular work on live sites in coal mining and port operations.</p>
      <p>We are proud to support local employers and build a safer regional workforce.</p>
      <p><b>Training that reflects real sites, real plant and real risk.</b></p>
    </div>
    <div class="photo" role="img" aria-label="Green scaffolding and crane structure against the sky" style="left:0;top:612px;width:496px;height:84px;background:linear-gradient(90deg,#6f9a34 0%,#9bcb3c 50%,#c9d9b0 100%)"></div>
    <div class="footer"><span>www.vantageskills.com.au</span><span>Page 03</span></div>
  </section>

  <!-- Key personnel -->
  <section class="page page--people">
    <h2 class="section-title">3. KEY PERSONNEL</h2>
    <div class="section-rule"></div>
    <div class="person__name" style="top:66px">DANA WHITLOCK <span>General Manager</span></div>
    <div class="photo" role="img" aria-label="Portrait photograph of the general manager" style="left:34px;top:86px;width:150px;height:150px;background:linear-gradient(180deg,#cfd8c0 0%,#c98a55 60%,#8a5a38 100%)"></div>
    <div class="col" style="left:250px;top:86px;width:214px">
      <div class="person__label">Key Qualifications</div>
      <p>Dana holds trainer and assessor qualifications and high-risk work licences across cranes, rigging and elevated platforms.</p>
      <ul class="ticks">
        <li>Diploma of Work Health and Safety</li><li>Certificate IV in Training and Assessment</li><li>Dogging and rigging licences</li><li>Mobile crane licence</li>
      </ul>
    </div>
    <div class="col" style="left:34px;top:260px;width:205px">
      <div class="person__label">Key Responsibilities</div>
      <ul class="ticks">
        <li>Leads all training and assessment staff</li><li>Maintains compliance and quality systems</li>
      </ul>
      <div class="person__label">Experience</div>
      <p>Over twenty years in mining and port operations, from plant operator to site trainer.</p>
      <ul class="ticks">
        <li>Site trainer at a coal mine</li><li>Crane operator at a bulk port</li><li>Safety advisor for civil works</li><li>Assessor for regional employers</li>
      </ul>
    </div>
    <div class="col" style="left:259px;top:260px;width:205px">
      <ul class="ticks">
        <li>Manages client relationships</li><li>Plans onsite course schedules</li><li>Reviews learner outcomes</li>
      </ul>
      <ul class="ticks" style="margin-top:30px">
        <li>Member of industry safety groups</li><li>Mentor to new trainers and assessors</li><li>Regular work on live mine sites</li><li>First aid and emergency response</li>
      </ul>
    </div>
    <div class="footer"><span>www.vantageskills.com.au</span><span>Page 04</span></div>
  </section>

  <!-- Back cover -->
  <section class="page page--back">
    <div class="photo" role="img" aria-label="Black and white photo of a crane and green scaffolding beside an industrial building" style="left:0;top:0;width:496px;height:470px;background:linear-gradient(180deg,#d6d6d6 0%,#9a9a9a 55%,#4a4a4a 100%)"></div>
    <div class="photo" style="left:0;top:0;width:120px;height:470px;background:linear-gradient(180deg,rgba(155,203,60,.85),rgba(95,143,28,.85))" role="img" aria-label="Green tinted scaffolding column"></div>
    <div class="brand" style="left:178px;top:540px"><span class="brand__dot"></span>VANTAGE SKILLS</div>
    <div class="back__contact">
      <div><svg width="10" height="10" viewBox="0 0 24 24"><path d="M6.6 10.8a15 15 0 006.6 6.6l2.2-2.2a1 1 0 011-.25 11.4 11.4 0 003.6.57 1 1 0 011 1V20a1 1 0 01-1 1A17 17 0 013 4a1 1 0 011-1h3.5a1 1 0 011 1 11.4 11.4 0 00.57 3.6 1 1 0 01-.25 1z" fill="#9bcb3c"/></svg>(07) 4950 2218</div>
      <div><svg width="10" height="10" viewBox="0 0 24 24"><path d="M3 5h18v14H3z" fill="none" stroke="#9bcb3c" stroke-width="2"/><path d="M3 5l9 8 9-8" fill="none" stroke="#9bcb3c" stroke-width="2"/></svg>admin@vantageskills.com.au</div>
      <div><svg width="10" height="10" viewBox="0 0 24 24"><circle cx="12" cy="12" r="9" fill="none" stroke="#9bcb3c" stroke-width="2"/><path d="M3 12h18M12 3c3 3 3 15 0 18M12 3c-3 3-3 15 0 18" fill="none" stroke="#9bcb3c" stroke-width="1.5"/></svg>www.vantageskills.com.au</div>
      <div><svg width="10" height="10" viewBox="0 0 24 24"><path d="M12 2a7 7 0 00-7 7c0 5 7 13 7 13s7-8 7-13a7 7 0 00-7-7zm0 9.5A2.5 2.5 0 1112 6.5a2.5 2.5 0 010 5z" fill="#9bcb3c"/></svg>12 Harbour Road, Mackay QLD 4740</div>
    </div>
    <div class="footer"><span></span><span></span></div>
  </section>

</div>
</body>
</html>
```